Velvet Basin Suites, a portable luxury restroom trailer company needs a landing page

We need a landing page for a luxury portable restroom trailer company. This should be modern, and simple - use any combination of Pantone colors: Warm Gray 1C, Black 7C, 7529c, 873C, 8003C

We rent these trailers for special events like weddings, private parties, festivals, family reunions, team building, wine tastings, beer tastings, food truck round-ups, etc.

An idea of the landing page is in the files below. Please use stock photography and placeholder text for now. The winning design will be given final content.

Requirements
Must have
• Multiple "Get Quote" buttons or a place for them to type in type of rental, how many people etc

```html
<!DOCTYPE html>
<html lang="en">
<head>
<meta charset="utf-8">
<title>Velvet Basin Suites — Portable Luxury Restroom Trailers</title>
<link href="https://fonts.googleapis.com/css2?family=Jost:wght@400;500;600;700&display=swap" rel="stylesheet">
<style>
:root{
  --navy:#3a4584;
  --navy-dark:#2e3770;
  --ink:#1d1d1f;
  --body:#3c3c44;
  --muted:#6d6d75;
  --warm:#f1f1f1;
  --line:#c9c9cf;
  --white:#ffffff;
}
*{margin:0;padding:0;box-sizing:border-box}
html,body{width:1200px;height:3604px;overflow:hidden}
body{position:relative;background:var(--white);font-family:'Jost',sans-serif;color:var(--ink)}
.abs{position:absolute}
a{color:inherit;text-decoration:none}

/* header */
.site-header{left:0;top:0;width:1200px;height:70px;background:var(--white);border-bottom:1px solid #e3e3e8}
.brand{left:175px;top:21px;font-size:20px;font-weight:600;color:var(--navy)}
.nav a{position:absolute;top:25px;font-size:15px;color:var(--ink)}
.nav .active{color:var(--navy)}
.nav-dots{left:667px;top:47px;display:flex;gap:4px}
.nav-dots i{width:4px;height:4px;border-radius:50%;background:var(--navy)}
.btn-talk{left:916px;top:18px;width:126px;height:34px;background:var(--navy);color:#fff;border-radius:4px;font-size:13px;font-weight:500;display:flex;align-items:center;justify-content:center;gap:6px}

/* hero */
.hero{left:0;top:70px;width:1200px;height:560px;overflow:hidden}
.hero-photo{position:absolute;inset:0;background:linear-gradient(160deg,#4c4a55 0%,#3a3d38 45%,#4d5439 100%)}
.hero-shade{position:absolute;inset:0;background:linear-gradient(90deg,rgba(20,20,30,.55),rgba(20,20,30,.1))}
.hero-trailer{left:637px;top:70px;width:427px;height:406px;background:linear-gradient(180deg,#f6f6f8,#dcdde2);border-radius:14px 14px 4px 4px}
.hero-title{left:158px;top:117px;font-size:38px;font-weight:700;line-height:46px;color:#fff;width:520px}
.hero-text{left:158px;top:218px;font-size:14px;line-height:23px;color:#fff;width:440px}
.btn-outline-light{left:160px;top:284px;width:138px;height:37px;border:1.5px solid #fff;border-radius:4px;color:#fff;font-size:13px;font-weight:500;display:flex;align-items:center;justify-content:center;gap:8px}
.slider-arrow{width:44px;height:44px;border-radius:50%;display:flex;align-items:center;justify-content:center}
.arrow-muted{background:rgba(255,255,255,.35)}
.arrow-solid{background:#fff}

/* section heads */
.section-head{left:0;width:1200px;text-align:center}
.section-head .kicker{font-size:14px;color:var(--muted)}
.section-head h2{font-size:31px;font-weight:600;color:var(--navy);line-height:40px}
.divider{display:flex;justify-content:center;gap:6px;margin-top:6px;align-items:center}
.divider span{width:28px;height:2px;background:var(--navy)}
.divider b{width:6px;height:6px;background:var(--navy)}

/* event cards */
.event-card{top:735px;width:280px;height:364px;background:#fff;border-radius:26px;box-shadow:0 4px 18px rgba(0,0,0,.08);overflow:hidden}
.event-photo{width:280px;height:182px;border-radius:26px 26px 26px 0}
.event-icon{position:absolute;left:19px;top:133px;width:70px;height:70px;background:var(--navy);border-radius:10px;display:flex;align-items:center;justify-content:center}
.event-card h3{position:absolute;left:19px;top:225px;font-size:19px;font-weight:500}
.event-card .rule{position:absolute;left:19px;top:256px;width:36px;height:2px;background:var(--navy)}
.event-card p{position:absolute;left:19px;top:265px;width:250px;font-size:14px;line-height:23px;color:var(--body)}
.btn-solid{background:var(--navy);color:#fff;border-radius:4px;font-size:13px;font-weight:500;display:flex;align-items:center;justify-content:center;gap:8px}

/* products */
.products-bg{left:0;top:1245px;width:1200px;height:1400px;background:var(--warm)}
.product-photo{border-radius:28px 28px 28px 0}
.product-back{background:var(--navy)}
.product-copy h3{font-size:20px;font-weight:500;line-height:27px;width:400px}
.product-copy .rule{width:36px;height:2px;background:var(--navy);margin:8px 0 14px}
.product-copy p{font-size:14px;line-height:23px;color:var(--body);width:380px}
.btn-outline{width:139px;height:36px;border:1.5px solid var(--navy);border-radius:4px;color:var(--navy);font-size:13px;font-weight:500;display:flex;align-items:center;justify-content:center;gap:8px;margin-top:26px}

/* gallery */
.gallery-tile{top:2817px;height:271px}
.gallery-caption{position:absolute;left:10px;top:10px;right:10px;bottom:10px;border:2px solid #fff;border-radius:20px;display:flex;flex-direction:column;align-items:center;justify-content:center;gap:16px;color:#fff;font-size:17px;font-weight:500;background:rgba(58,69,132,.55)}

/* quote */
.quote-band{left:160px;top:3158px;width:882px;height:236px;background:linear-gradient(135deg,var(--navy),var(--navy-dark));border-radius:26px;text-align:center;color:#fff}
.quote-band h2{margin-top:42px;font-size:31px;font-weight:600}
.quote-band p{margin:10px auto 0;width:470px;font-size:14px;line-height:23px}
.quote-band .btn-outline-light{position:absolute;left:372px;top:153px}

/* footer */
.footer-nav{left:0;top:3428px;width:1200px;display:flex;justify-content:center;gap:16px;font-size:14px;color:var(--ink)}
.footer-nav .active{color:var(--navy)}
.footer-nav .sep{color:#b9b9c0}
.social{top:3479px;width:34px;height:34px;border-radius:50%;background:#bcbcc4}
.social.first{background:var(--ink)}
.copyright{left:0;top:3555px;width:1200px;text-align:center;font-size:12px;color:var(--muted)}
</style>
</head>
<body>

<header class="abs site-header">
  <a class="abs brand" href="#">Velvet Basin Suites</a>
  <nav class="nav">
    <a class="active" style="left:652px" href="#">Events</a>
    <a style="left:729px" href="#">Products</a>
    <a style="left:822px" href="#">Contacts</a>
  </nav>
  <div class="abs nav-dots"><i></i><i></i><i></i></div>
  <a class="abs btn-talk" href="#">
    <svg width="13" height="13" viewBox="0 0 14 14" fill="none" stroke="#fff" stroke-width="1.6"><path d="M2 9V7a5 5 0 0 1 10 0v2"/><rect x="1.5" y="8" width="3" height="4" rx="1" fill="#fff"/><rect x="9.5" y="8" width="3" height="4" rx="1" fill="#fff"/></svg>
    Let's Talk
  </a>
</header>

<section class="abs hero">
  <div class="hero-photo" role="img" aria-label="Evening backyard with lawn chairs and a house"></div>
  <div class="hero-shade"></div>
  <div class="abs hero-trailer" role="img" aria-label="White luxury restroom trailer with steps"></div>
  <h1 class="abs hero-title">Portable Luxury Restroom Trailer for any occasion</h1>
  <p class="abs hero-text">Lorem ipsum dolor sit amet consectetur adipiscing elit sed do eiusmod tempor incididunt ut labore et dolore magna.</p>
  <a class="abs btn-outline-light" href="#">Contact Us <svg width="10" height="11" viewBox="0 0 10 11"><path d="M1 0l9 5.5L1 11z" fill="#fff"/></svg></a>
  <div class="abs slider-arrow arrow-muted" style="left:87px;top:195px"><svg width="14" height="12" viewBox="0 0 14 12" fill="none" stroke="#fff" stroke-width="2"><path d="M13 6H2M6 1L1 6l5 5"/></svg></div>
  <div class="abs slider-arrow arrow-solid" style="left:1074px;top:195px"><svg width="14" height="12" viewBox="0 0 14 12" fill="none" stroke="#3a4584" stroke-width="2"><path d="M1 6h11M8 1l5 5-5 5"/></svg></div>
  <svg class="abs" style="left:0;top:400px" width="1200" height="160" viewBox="0 0 1200 160" preserveAspectRatio="none">
    <path d="M0 95 C200 70 300 0 480 10 C700 20 800 120 1200 85 V160 H0Z" fill="#a9a9ae"/>
    <path d="M0 80 C200 50 300 -5 480 5 C700 15 800 100 1200 55 V160 H0Z" fill="#3a4584"/>
    <path d="M0 110 C200 85 300 20 480 30 C700 40 820 150 1200 160 V160 H0Z" fill="#fff"/>
  </svg>
</section>

<div class="abs section-head" style="top:624px">
  <div class="kicker">We rent these trailers for</div>
  <h2>Special Events</h2>
  <div class="divider"><span></span><b></b><span></span></div>
</div>

<article class="abs event-card" style="left:160px">
  <div class="event-photo" role="img" aria-label="Lit wedding gazebo by the sea at dusk" style="background:linear-gradient(180deg,#5a5f86,#7d6b7c 55%,#2d2e3d)"></div>
  <div class="event-icon"><svg width="42" height="42" viewBox="0 0 42 42" fill="none" stroke="#fff" stroke-width="2"><circle cx="16" cy="25" r="10"/><circle cx="26" cy="25" r="10"/><path d="M18 6l3 4 3-4"/></svg></div>
  <h3>Weddings</h3><div class="rule"></div>
  <p>Lorem ipsum dolor sit amet consec adipiscing elit sed do eiusmod sito tempor incididunt ut labore et</p>
</article>
<article class="abs event-card" style="left:459px">
  <div class="event-photo" role="img" aria-label="Guests dancing at a private party" style="background:linear-gradient(180deg,#3f3328,#6e5a46 55%,#2b241e)"></div>
  <div class="event-icon"><svg width="42" height="42" viewBox="0 0 42 42" fill="none" stroke="#fff" stroke-width="2"><path d="M10 8h8l-1 10a3 3 0 0 1-6 0zM14 21v11M10 32h8"/><path d="M24 8h8l-1 10a3 3 0 0 1-6 0zM28 21v11M24 32h8"/></svg></div>
  <h3>Private Parties</h3><div class="rule"></div>
  <p>Lorem ipsum dolor sit amet consec adipiscing elit sed do eiusmod sito tempor incididunt ut labore et</p>
</article>
<article class="abs event-card" style="left:760px">
  <div class="event-photo" role="img" aria-label="Family gathered at outdoor tables" style="background:linear-gradient(180deg,#4d6a3b,#7a7f6a 55%,#4b4f45)"></div>
  <div class="event-icon"><svg width="42" height="42" viewBox="0 0 42 42" fill="none" stroke="#fff" stroke-width="2"><circle cx="13" cy="17" r="4"/><circle cx="29" cy="17" r="4"/><circle cx="21" cy="21" r="4"/><path d="M6 32c0-5 3-8 7-8M36 32c0-5-3-8-7-8M13 34c0-5 3-8 8-8s8 3 8 8"/></svg></div>
  <h3>Family Reunions</h3><div class="rule"></div>
  <p>Lorem ipsum dolor sit amet consec adipiscing elit sed do eiusmod sito tempor incididunt ut labore et</p>
</article>

<a class="abs btn-solid" style="left:521px;top:1135px;width:161px;height:37px" href="#">View All Events <svg width="10" height="11" viewBox="0 0 10 11"><path d="M1 0l9 5.5L1 11z" fill="#fff"/></svg></a>

<div class="abs products-bg"></div>
<div class="abs section-head" style="top:1306px">
  <div class="kicker">View Our</div>
  <h2>Products</h2>
  <div class="divider"><span></span><b></b><span></span></div>
</div>

<!-- product 1 -->
<div class="abs product-back" style="left:406px;top:1505px;width:201px;height:214px;border-radius:0 0 28px 0"></div>
<div class="abs product-photo" role="img" aria-label="White restroom trailer with stair rails among trees" style="left:160px;top:1435px;width:431px;height:270px;background:linear-gradient(170deg,#6f7f57,#c9cbc7 45%,#8a8a86)"></div>
<div class="abs" style="left:245px;top:1713px;width:153px;height:17px;border-bottom:2px solid var(--navy);border-right:2px solid var(--navy)"></div>
<div class="abs product-copy" style="left:665px;top:1454px">
  <h3>At vero eos et accusamus et iusto odio dignissimos ducimus qui praesentium</h3><div class="rule"></div>
  <p>Lorem ipsum dolor sit amet, consectetur adipiscing sin elit, sed do eiusmod tempor incididunt ut labore et esse dolore magna aliqua. Ut enim ad minim veniam, quis to nostrud exercitation ullamco laboris nisi ut aliquip deri ea commodo consequat uis aute irure dolor volupta.</p>
  <a class="btn-outline" href="#">Learn More <svg width="10" height="11" viewBox="0 0 10 11"><path d="M1 0l9 5.5L1 11z" fill="#3a4584"/></svg></a>
</div>
<svg class="abs" style="left:505px;top:1730px" width="100" height="70" fill="none" stroke="#8a8a92" stroke-width="1.2" stroke-dasharray="4 4"><path d="M8 4 C20 40 50 55 90 64"/><path d="M84 58l7 6-8 3" stroke-dasharray="none"/></svg>

<!-- product 2 -->
<div class="abs product-back" style="left:593px;top:1868px;width:200px;height:220px;border-radius:0 0 0 28px"></div>
<div class="abs product-photo" role="img" aria-label="White enclosed trailer parked beside palm trees" style="left:610px;top:1803px;width:432px;height:269px;border-radius:28px 28px 0 28px;background:linear-gradient(180deg,#cfd8e3,#e6e8ea 45%,#6c6f6e)"></div>
<div class="abs" style="left:801px;top:2080px;width:153px;height:17px;border-top:2px solid var(--navy);border-left:2px solid var(--navy)"></div>
<div class="abs product-copy" style="left:158px;top:1823px">
  <h3>At vero eos et accusamus et iusto odio dignissimos ducimus qui praesentium</h3><div class="rule"></div>
  <p>Lorem ipsum dolor sit amet, consectetur adipiscing sin elit, sed do eiusmod tempor incididunt ut labore et esse dolore magna aliqua. Ut enim ad minim veniam, quis to nostrud exercitation ullamco laboris nisi ut aliquip deri ea commodo consequat uis aute irure dolor volupta.</p>
  <a class="btn-outline" href="#">Learn More <svg width="10" height="11" viewBox="0 0 10 11"><path d="M1 0l9 5.5L1 11z" fill="#3a4584"/></svg></a>
</div>
<svg class="abs" style="left:595px;top:2100px" width="100" height="70" fill="none" stroke="#8a8a92" stroke-width="1.2" stroke-dasharray="4 4"><path d="M90 4 C80 40 50 55 8 64"/><path d="M14 58l-7 6 8 3" stroke-dasharray="none"/></svg>

<!-- product 3 -->
<div class="abs product-back" style="left:406px;top:2261px;width:201px;height:214px;border-radius:0 0 28px 0"></div>
<div class="abs product-photo" role="img" aria-label="Green restroom trailer with separate entrances" style="left:160px;top:2191px;width:431px;height:270px;background:linear-gradient(175deg,#6d8a56,#1f5a3e 40%,#2d5c43 80%,#9a9a97)"></div>
<div class="abs" style="left:245px;top:2469px;width:153px;height:17px;border-bottom:2px solid var(--navy);border-right:2px solid var(--navy)"></div>
<div class="abs product-copy" style="left:665px;top:2211px">
  <h3>At vero eos et accusamus et iusto odio dignissimos ducimus qui praesentium</h3><div class="rule"></div>
  <p>Lorem ipsum dolor sit amet, consectetur adipiscing sin elit, sed do eiusmod tempor incididunt ut labore et esse dolore magna aliqua. Ut enim ad minim veniam, quis to nostrud exercitation ullamco laboris nisi ut aliquip deri ea commodo consequat uis aute irure dolor volupta.</p>
  <a class="btn-outline" href="#">Learn More <svg width="10" height="11" viewBox="0 0 10 11"><path d="M1 0l9 5.5L1 11z" fill="#3a4584"/></svg></a>
</div>

<svg class="abs" style="left:0;top:2540px" width="1200" height="130" viewBox="0 0 1200 130" preserveAspectRatio="none">
  <path d="M0 60 C150 100 300 130 500 90 C700 50 950 -10 1200 40 V130 H0Z" fill="#fff"/>
</svg>
<div class="abs" style="left:0;top:2660px;width:1200px;height:944px;background:#fff"></div>

<div class="abs section-head" style="top:2688px">
  <div class="kicker">Have a look our</div>
  <h2>Restroom Gallery</h2>
  <div class="divider"><span></span><b></b><span></span></div>
</div>

<div class="abs gallery-tile" role="img" aria-label="Bright bathroom with grey vanity and toilet" style="left:0;width:365px;border-radius:0 26px 26px 0;background:linear-gradient(160deg,#eceae6,#cfcfcf 55%,#6e7684)"></div>
<div class="abs gallery-tile" style="left:374px;width:452px;border-radius:26px;background:linear-gradient(160deg,#5d6387,#3f466f)" role="img" aria-label="Marble bathroom with round mirrors">
  <div class="gallery-caption">
    <svg width="38" height="38" viewBox="0 0 38 38" fill="none" stroke="#fff" stroke-width="2.4"><path d="M2 10V2h8M28 2h8v8M36 28v8h-8M10 36H2v-8"/><circle cx="18" cy="17" r="6"/><path d="M22 21l5 5M18 14v6M15 17h6"/></svg>
    Image title goes here
  </div>
</div>
<div class="abs gallery-tile" role="img" aria-label="Stone vessel sink with black wall taps" style="left:834px;width:366px;border-radius:26px 0 0 26px;background:linear-gradient(180deg,#d9d9d6,#bdbcb8 50%,#6f655e 75%,#ececec)"></div>
<div class="abs slider-arrow" style="left:82px;top:2932px;background:rgba(58,69,132,.75)"><svg width="14" height="12" viewBox="0 0 14 12" fill="none" stroke="#fff" stroke-width="2"><path d="M13 6H2M6 1L1 6l5 5"/></svg></div>
<div class="abs slider-arrow" style="left:1074px;top:2932px;background:rgba(58,69,132,.75)"><svg width="14" height="12" viewBox="0 0 14 12" fill="none" stroke="#fff" stroke-width="2"><path d="M1 6h11M8 1l5 5-5 5"/></svg></div>

<svg class="abs" style="left:0;top:3220px" width="1200" height="384" viewBox="0 0 1200 384" preserveAspectRatio="none">
  <path d="M0 60 C300 10 700 0 1200 40 V384 H0Z" fill="#f1f1f1"/>
</svg>

<section class="abs quote-band">
  <h2>Contact us For A Quote</h2>
  <p>Lorem ipsum dolor sit amet consectetur adipiscing sin elit sed do eiusmod tempor incididunt ut labore et esse dolore magna</p>
  <a class="btn-outline-light" href="#">Contact Us <svg width="10" height="11" viewBox="0 0 10 11"><path d="M1 0l9 5.5L1 11z" fill="#fff"/></svg></a>
</section>

<nav class="abs footer-nav">
  <a class="active" href="#">Events</a><span class="sep">|</span>
  <a href="#">Products</a><span class="sep">|</span>
  <a href="#">Contacts</a>
</nav>
<a class="abs social first" style="left:518px" href="#" aria-label="Social profile one"></a>
<a class="abs social" style="left:561px" href="#" aria-label="Social profile two"></a>
<a class="abs social" style="left:606px" href="#" aria-label="Social profile three"></a>
<a class="abs social" style="left:649px" href="#" aria-label="Social profile four"></a>
<p class="abs copyright">Copyright © 2022 Company Name Goes Here. All Rights Reserved.</p>

</body>
</html>
```